5 website banners (slides show)

We need 5 website sliding banners created for a website all about internet safety. The topics for each banner are:

Cyberbullying
Fraud
seniors
social networking

Sizes: 953 pixels x 281 pixels

I have stock images to use or feel free to use your own or one I can purchase from pixelvarro.example.

Industry/Entity Type

Internet

```html
<!DOCTYPE html>
<html lang="en">
<head>
<meta charset="utf-8">
<title>Seniors – Internet Safety Banner</title>
<link rel="stylesheet" href="https://fonts.googleapis.com/css2?family=Nunito:wght@400;700&display=swap">
<style>
  :root {
    --page-white: #ffffff;
    --field-grey: #f2f3f4;
    --band-dark: #1b5ea8;
    --band-light: #64a3e8;
    --text-white: #ffffff;
    --photo-sky: #dbe9ef;
    --photo-sky-deep: #c4d8e1;
    --photo-warm: #c9a58c;
    --photo-cream: #efe9e1;
  }
  html, body {
    margin: 0;
    padding: 0;
    width: 1200px;
    height: 354px;
    overflow: hidden;
    background: var(--page-white);
  }
  .banner {
    position: relative;
    width: 1200px;
    height: 354px;
    overflow: hidden;
    background: linear-gradient(90deg, var(--field-grey) 0%, var(--page-white) 42%);
    font-family: "Nunito", Arial, sans-serif;
  }
  .banner__photo {
    position: absolute;
    top: 0;
    right: 0;
    width: 700px;
    height: 354px;
    background:
      radial-gradient(ellipse 46% 62% at 48% 62%, var(--photo-warm) 0%, rgba(201,165,140,0) 100%),
      linear-gradient(160deg, var(--photo-sky) 0%, var(--photo-sky-deep) 45%, var(--photo-cream) 100%);
    -webkit-mask-image: linear-gradient(90deg, transparent 0%, #000 22%);
    mask-image: linear-gradient(90deg, transparent 0%, #000 22%);
  }
  .banner__bands {
    position: absolute;
    left: 58px;
    top: 111px;
    width: 453px;
    height: 125px;
  }
  .banner__title {
    position: absolute;
    left: 86px;
    top: 118px;
    margin: 0;
    font-size: 42px;
    font-weight: 700;
    color: var(--text-white);
    line-height: 60px;
  }
  .banner__subtitle {
    position: absolute;
    left: 86px;
    top: 195px;
    margin: 0;
    font-size: 21px;
    font-weight: 400;
    color: var(--text-white);
    line-height: 30px;
    white-space: nowrap;
  }
</style>
</head>
<body>
  <section class="banner">
    <div class="banner__photo" role="img" aria-label="Photo of a smiling family gathered around a laptop"></div>
    <svg class="banner__bands" viewBox="0 0 453 125" aria-hidden="true">
      <polygon points="0,0 453,0 428,75 0,75" fill="var(--band-dark)"/>
      <polygon points="0,75 391,75 369,124 0,124" fill="var(--band-light)"/>
    </svg>
    <h1 class="banner__title">Seniors</h1>
    <p class="banner__subtitle">Lorem ipsum dolor consectetue</p>
  </section>
</body>
</html>
```